Redesign of Website

We need an overhaul of our website. I've attached our current logo files. Please visit www.pelvorix.com for our current website for information about our company. We are looking for the same type of website (information-based only) so no need for any online store, payments, interactive stuff or anything like that...basically looking for a fresh new look! Also please make sure this design will be mobile-friendly. Thanks!

```html
<!DOCTYPE html>
<html lang="en">
<head>
<meta charset="utf-8">
<title>Pelvorix Consultants</title>
<link href="https://fonts.googleapis.com/css2?family=Work+Sans:wght@400;500;600;700&family=Roboto:wght@400;500&display=swap" rel="stylesheet">
<style>
:root{
  --blue:#0b3f8c;
  --blue-dark:#093474;
  --green:#8fca92;
  --green-soft:#e6f3e7;
  --ink:#333a44;
  --muted:#6d737b;
  --line:#e3e6ea;
  --white:#ffffff;
}
*{margin:0;padding:0;box-sizing:border-box}
html,body{width:1200px;height:2727px;overflow:hidden;background:var(--white)}
body{position:relative;font-family:"Roboto",Arial,sans-serif;color:var(--ink)}
.abs{position:absolute}
.brand{font-family:"Work Sans",Arial,sans-serif;font-weight:700;color:var(--blue);font-size:34px;letter-spacing:-0.5px;display:flex;align-items:center;gap:10px}
.brand .dot{width:14px;height:14px;border-radius:50%;background:var(--green)}
.brand small{display:block;font-size:12px;letter-spacing:2px;font-weight:700;margin-top:-4px}

/* header */
.phone-band{left:836px;top:0;width:364px;height:537px;background:var(--blue)}
.phone-top{left:870px;top:24px;color:#fff;font:600 24px "Work Sans",sans-serif;display:flex;align-items:center;gap:10px}
.nav{left:423px;top:34px;display:flex;gap:30px;align-items:center;font-size:11px;color:var(--ink);text-transform:uppercase}
.btn-quote{background:var(--green);color:#fff;border-radius:14px;padding:6px 18px;font-size:10px}

/* hero */
.hero{left:160px;top:85px;width:878px;height:452px;background:#fff;padding:12px;box-shadow:0 4px 18px rgba(0,0,0,.18)}
.hero-photo{width:100%;height:100%;background:linear-gradient(120deg,#5c5f63 0%,#7b7770 45%,#a38f7c 75%,#6b665f 100%);position:relative}
.hero-copy{position:absolute;left:29px;top:256px;width:440px;color:#fff}
.hero-copy h1{font:700 26px "Work Sans",sans-serif;margin-bottom:14px}
.hero-copy p{font-size:12.5px;line-height:1.55}
.btn-read{display:inline-flex;align-items:center;gap:8px;margin-top:26px;border:1px solid var(--green);color:#fff;border-radius:14px;padding:5px 8px 5px 20px;font-size:10px;text-transform:uppercase}
.btn-read i{width:16px;height:16px;border-radius:50%;background:var(--green);display:inline-block}
.arrow{top:292px}

/* section heads */
.kicker{width:1200px;text-align:center;color:var(--green);font:500 12px "Work Sans",sans-serif;letter-spacing:3px;text-transform:uppercase}
.title{width:1200px;text-align:center;font:500 26px "Work Sans",sans-serif;color:#3c4148}

/* service cards */
.card{width:278px;height:224px;border:1px solid var(--line);background:#fff;text-align:center;padding:22px 26px 0;overflow:hidden}
.card h3{font:600 15px "Work Sans",sans-serif;margin:18px 0 14px;color:#3c4148;line-height:1.25}
.card p{font-size:11.5px;line-height:1.65;color:var(--muted)}
.card .icon{width:48px;height:48px;margin:0 auto}
.card .corner{position:absolute;right:-22px;bottom:-22px;width:56px;height:56px;border-radius:50%;background:var(--green)}
.card .corner svg{position:absolute;left:12px;top:14px}
.card.active{background:var(--blue);border-color:var(--blue)}
.card.active h3,.card.active p{color:#fff}

/* about */
.about-band{left:0;top:1238px;width:1200px;height:560px;background:linear-gradient(100deg,#3f6a4c 0%,#5f8b63 40%,#4d7753 70%,#2f5236 100%)}
.about-card{left:462px;top:1313px;width:576px;height:409px;background:#fff;padding:34px 38px;overflow:hidden;box-shadow:0 4px 18px rgba(0,0,0,.15)}
.about-card .k{color:var(--green);font:500 12px "Work Sans",sans-serif;letter-spacing:3px}
.about-card h2{font:500 27px "Work Sans",sans-serif;margin:6px 0 18px}
.about-card p{font-size:11.5px;line-height:1.75;color:#4b5058;margin-bottom:14px;position:relative}
.bubble{position:absolute;border-radius:50%;background:var(--green-soft)}
.btn-more{display:inline-flex;align-items:center;gap:10px;border:1px solid var(--blue);border-radius:14px;padding:5px 6px 5px 18px;font-size:10px;color:var(--blue);text-transform:uppercase;position:relative}
.btn-more i{width:18px;height:18px;border-radius:50%;background:var(--blue);display:inline-block}

/* contact */
.contact-band{left:0;top:2214px;width:1200px;height:206px;background:var(--blue)}
.form-card{left:160px;top:1962px;width:578px;height:309px;background:#fff;padding:30px 30px;box-shadow:0 4px 16px rgba(0,0,0,.12)}
.field{border:1px solid var(--line);height:30px;font-size:11px;color:var(--muted);padding:8px 10px;position:absolute}
.btn-send{position:absolute;left:30px;top:252px;width:518px;height:28px;background:var(--green);border-radius:14px;color:#fff;font-size:11px;text-align:center;line-height:28px}
.map{left:760px;top:1962px;width:278px;height:309px;background:linear-gradient(160deg,#eef1ee 0%,#e3ebe3 50%,#d7e6f2 100%)}
.info{top:2310px;display:flex;gap:18px;color:#fff}
.info .ring{width:56px;height:56px;border-radius:50%;background:#fff;display:flex;align-items:center;justify-content:center;flex:none}
.info h4{font:600 13px "Work Sans",sans-serif;margin:4px 0 6px}
.info p{font-size:11.5px;line-height:1.55}

/* footer */
.foot-h{font:500 13px "Work Sans",sans-serif;letter-spacing:1px;text-transform:uppercase;color:#3c4148}
.foot-list{list-style:none;font-size:11px;color:#555;line-height:2.1;margin-top:16px}
.foot-list li::before{content:"› ";color:var(--ink)}
.foot-list li.on{color:var(--green)}
.social{display:flex;gap:14px}
.social i{width:26px;height:26px;border-radius:50%;background:var(--blue);display:block}
.newsletter p{font-size:11px;color:#555;line-height:1.6;margin:16px 0 12px;width:210px}
.email{width:206px;height:28px;border:1px solid var(--line);border-radius:14px;font-size:10.5px;color:var(--muted);padding:7px 12px;position:relative}
.bottom-bar{left:0;top:2690px;width:1200px;height:37px;background:var(--blue);color:#fff;font-size:10.5px;padding:12px 160px}
</style>
</head>
<body>

<!-- header -->
<div class="abs phone-band"></div>
<div class="abs brand" style="left:160px;top:16px"><div>Pelvorix<small>CONSULTANTS</small></div><span class="dot"></span></div>
<nav class="abs nav"><span>Home</span><span>About Us</span><span>Services ˅</span><span>Contact</span><span class="btn-quote">Request a Quote</span></nav>
<div class="abs phone-top">
  <svg width="20" height="20" viewBox="0 0 24 24"><path fill="#fff" d="M6.6 10.8a15 15 0 0 0 6.6 6.6l2.2-2.2c.3-.3.7-.4 1-.2 1.1.4 2.3.6 3.6.6.6 0 1 .4 1 1V20c0 .6-.4 1-1 1A17 17 0 0 1 3 4c0-.6.4-1 1-1h3.5c.6 0 1 .4 1 1 0 1.3.2 2.5.6 3.6.1.3 0 .7-.2 1z"/></svg>
  555-014-2290
</div>

<!-- hero -->
<div class="abs hero">
  <div class="hero-photo" role="img" aria-label="Photo of three professionals reviewing property plans around a small model house">
    <div class="hero-copy">
      <h1>Property Condition Reports</h1>
      <p>Before moving ahead on any loan approval, financial institutions need to know the condition of existing structures. Our professional staff will give you the details you need to make sound business decisions</p>
      <span class="btn-read">Read More <i></i></span>
    </div>
  </div>
</div>
<svg class="abs arrow" style="left:44px" width="16" height="32" viewBox="0 0 16 32"><path d="M14 2 2 16l12 14" fill="none" stroke="#9aa0a6" stroke-width="2"/></svg>
<svg class="abs arrow" style="left:1138px" width="16" height="32" viewBox="0 0 16 32"><path d="M2 2l12 14L2 30" fill="none" stroke="#fff" stroke-width="2"/></svg>

<!-- services -->
<div class="abs kicker" style="left:0;top:593px">Our Services</div>
<div class="abs title" style="left:0;top:610px">We offers the following services</div>

<div class="abs card active" style="left:160px;top:691px">
  <svg class="icon" viewBox="0 0 48 48"><g fill="none" stroke="#fff" stroke-width="1.6"><rect x="12" y="8" width="22" height="30"/><path d="M16 4h22v30"/><path d="M16 16h14M16 21h14M16 26h14M16 31h9"/></g></svg>
  <h3>Property Condition Reports</h3>
  <p>Before moving ahead on any loan approval, financial institutions need to know the condition of existing structures.</p>
  <span class="corner"><svg width="16" height="12"><path d="M1 6h13M9 1l5 5-5 5" fill="none" stroke="#fff" stroke-width="1.6"/></svg></span>
</div>
<div class="abs card" style="left:460px;top:691px">
  <svg class="icon" viewBox="0 0 48 48"><g fill="none" stroke="#8fca92" stroke-width="1.6"><rect x="8" y="6" width="26" height="34"/><circle cx="21" cy="17" r="6"/><path d="M12 30h18M12 35h12"/><rect x="30" y="24" width="12" height="16"/><path d="M33 28h6M33 32h6"/></g></svg>
  <h3>Plan &amp; Cost Reviews</h3>
  <p>Our Plan &amp; Cost Reviews provide lending institutions with expert analysis of new construction projects before loan</p>
  <span class="corner"><svg width="16" height="12"><path d="M1 6h13M9 1l5 5-5 5" fill="none" stroke="#fff" stroke-width="1.6"/></svg></span>
</div>
<div class="abs card" style="left:762px;top:691px">
  <svg class="icon" viewBox="0 0 48 48"><g fill="none" stroke="#8fca92" stroke-width="1.6"><path d="M8 22 24 8l16 14"/><path d="M12 19v20h24V19"/><circle cx="24" cy="27" r="5"/><path d="M24 24v6"/></g></svg>
  <h3>Construction Funding Inspections</h3>
  <p>Lending institutions rarely have employees with the expertise needed to evaluate multiple stages of site construction</p>
  <span class="corner"><svg width="16" height="12"><path d="M1 6h13M9 1l5 5-5 5" fill="none" stroke="#fff" stroke-width="1.6"/></svg></span>
</div>
<div class="abs card" style="left:311px;top:938px">
  <svg class="icon" viewBox="0 0 48 48"><g fill="none" stroke="#8fca92" stroke-width="1.6"><rect x="5" y="8" width="38" height="26"/><path d="M18 40h12M24 34v6"/><path d="M10 28l8-8 6 5 12-11"/></g></svg>
  <h3>Environmental Transaction Screens</h3>
  <p>Environmental Transaction Screens provide an economical but meaningful alternative for smaller properties such</p>
  <span class="corner"><svg width="16" height="12"><path d="M1 6h13M9 1l5 5-5 5" fill="none" stroke="#fff" stroke-width="1.6"/></svg></span>
</div>
<div class="abs card" style="left:611px;top:938px">
  <svg class="icon" viewBox="0 0 48 48"><g fill="none" stroke="#8fca92" stroke-width="1.6"><rect x="10" y="6" width="24" height="32"/><path d="M15 14h14M15 19h14M15 24h8"/><rect x="24" y="24" width="16" height="16"/><path d="M28 34v-4M32 34v-6M36 34v-2"/></g></svg>
  <h3>Phase 1 Environmental Assessment</h3>
  <p>With reasonable pricing and a quick turn-around, we provide comprehensive Phase 1 reports. Our reports provide</p>
  <span class="corner"><svg width="16" height="12"><path d="M1 6h13M9 1l5 5-5 5" fill="none" stroke="#fff" stroke-width="1.6"/></svg></span>
</div>

<!-- about -->
<div class="abs about-band" role="img" aria-label="Green-toned photo of a building under construction with scaffolding and a worker on site"></div>
<div class="abs about-card">
  <span class="bubble" style="right:50px;top:-20px;width:64px;height:64px"></span>
  <span class="bubble" style="right:6px;top:30px;width:46px;height:46px"></span>
  <span class="bubble" style="right:-30px;bottom:-40px;width:120px;height:120px"></span>
  <div class="k">OUR COMPANY</div>
  <h2>About Pelvorix Consultants</h2>
  <p>With over 25 years experience we provide customized and comprehensive inspection services to financial institutions involved in construction and loan management in the tri-state region and surrounding areas.</p>
  <p>The firm's professional staff bring years of engineering, environmental, building, and real estate experience to work for our clients.</p>
  <p>Pelvorix provides our clients with in-depth plan &amp; cost, construction funding, environmental and property condition reports.</p>
  <p>Pelvorix will give you the essential facts that are critical for solid business decision making and ongoing loan management.</p>
  <span class="btn-more">Know More About Us <i></i></span>
</div>

<!-- contact -->
<div class="abs kicker" style="left:0;top:1871px">Contact Us</div>
<div class="abs title" style="left:0;top:1888px">Request A Call Back</div>
<div class="abs contact-band"></div>
<div class="abs form-card">
  <div class="field" style="left:30px;top:30px;width:248px">Your Name</div>
  <div class="field" style="left:300px;top:30px;width:248px">Email</div>
  <div class="field" style="left:30px;top:82px;width:518px">Phone</div>
  <div class="field" style="left:30px;top:134px;width:518px;height:92px">Message</div>
  <div class="btn-send">SEND →</div>
</div>
<div class="abs map" role="img" aria-label="Street map showing the office location with nearby lakes and roads"></div>

<div class="abs info" style="left:160px">
  <span class="ring"><svg width="20" height="24" viewBox="0 0 20 24"><path d="M10 23s8-8 8-13a8 8 0 0 0-16 0c0 5 8 13 8 13z" fill="none" stroke="#8fca92" stroke-width="1.8"/><circle cx="10" cy="10" r="3" fill="none" stroke="#8fca92" stroke-width="1.8"/></svg></span>
  <div><h4>Address:</h4><p>48 Larkmoor Ave, Suite 112,<br>Brennfield Township,<br>NJ 07990</p></div>
</div>
<div class="abs info" style="left:460px">
  <span class="ring"><svg width="24" height="18" viewBox="0 0 24 18"><rect x="1" y="1" width="22" height="16" fill="none" stroke="#8fca92" stroke-width="1.8"/><path d="M1 1l11 9 11-9" fill="none" stroke="#8fca92" stroke-width="1.8"/></svg></span>
  <div><h4>E-mail:</h4><p>info@pelvorix.com<br>quotes@pelvorix.com<br>inspections@pelvorix.com</p></div>
</div>
<div class="abs info" style="left:762px">
  <span class="ring"><svg width="22" height="22" viewBox="0 0 24 24"><path fill="none" stroke="#8fca92" stroke-width="1.8" d="M6.6 10.8a15 15 0 0 0 6.6 6.6l2.2-2.2c.3-.3.7-.4 1-.2 1.1.4 2.3.6 3.6.6.6 0 1 .4 1 1V20c0 .6-.4 1-1 1A17 17 0 0 1 3 4c0-.6.4-1 1-1h3.5c.6 0 1 .4 1 1 0 1.3.2 2.5.6 3.6.1.3 0 .7-.2 1z"/></svg></span>
  <div><h4>Phone:</h4><p>555-014-2290</p></div>
</div>

<!-- footer -->
<div class="abs brand" style="left:160px;top:2452px;font-size:40px"><div>Pelvorix<small>CONSULTANTS</small></div><span class="dot"></span></div>
<div class="abs social" style="left:162px;top:2600px"><i></i><i></i><i></i><i></i></div>

<div class="abs" style="left:462px;top:2496px">
  <div class="foot-h">Quick Links</div>
  <ul class="foot-list"><li class="on">Home</li><li>About Us</li><li>Services</li><li>Contact</li></ul>
</div>
<div class="abs" style="left:611px;top:2496px">
  <div class="foot-h">Our Services</div>
  <ul class="foot-list"><li>Property Condition Reports</li><li>Plan &amp; Cost Reviews</li><li>Construction Funding Inspections</li><li>Environmental Transaction Screens</li><li>Phase 1 Environmental Assessment</li></ul>
</div>
<div class="abs newsletter" style="left:836px;top:2496px">
  <div class="foot-h">Newsletter</div>
  <p>Subscribe to our newsletter to get latest news and updates.</p>
  <div class="email">Enter your email
    <svg style="position:absolute;right:10px;top:7px" width="14" height="12" viewBox="0 0 14 12"><path d="M1 6 13 1 10 11 7 7z" fill="#8fca92"/></svg>
  </div>
</div>

<div class="abs bottom-bar">© Copyright Pelvorix Consultants 2019 | Privacy Policy | Terms of Use</div>

</body>
</html>
```